Whispers at Dawn, Quiet Devotions for Every Weary Heart Seeking Rest

I want a book cover design, The book is a prayer book. Pleas no design with only words. I want something creative and original. Something that attracts attention just by looking at the cover. Something powerful. This book is for people that are experiencing issues and need prayer. This book is also for those that want to pray and pray effectively. Not only will there be prayers. But they will learn the dynamics of prayer and how to pray effectively and from the right position. This book is filled with power yet effective prayers that will.have the ability to break bondages off people lives.
Below is some book covers that I found. I posted them to give an idea of what im looking for. Something that catches the attention of a reader.

Target Market(s)

Everyone, religious people

Industry/Entity Type

Religious

Font styles to use
Serif
Sans Serif

Requirements
Must have
• Creativity, originality,
Nice to have
• Professional looking. Powerful looking
Should not have
• Should not have just one color with big ole words across the whole book.

```html
<!DOCTYPE html>
<html lang="en">
<head>
<meta charset="utf-8">
<title>Whispers at Dawn – Cover</title>
<link href="https://fonts.googleapis.com/css2?family=Archivo+Black&family=Lato:wght@400&family=Montserrat:wght@700&display=swap" rel="stylesheet">
<style>
  :root {
    --page-bg: #ecebe8;
    --title-blue: #1f4f8f;
    --ink: #111417;
    --sky-white: #eef2f6;
    --sky-grey: #c9d3dd;
    --sky-blue: #4a9ad6;
    --deep-blue: #2f7cc6;
    --cross-blue: #3a86c4;
    --sun-yellow: #f2d836;
    --field-gold: #c9a93a;
    --grass-dark: #6b5a2a;
    --figure-teal: #6f8f86;
    --figure-dark: #3c4a46;
  }
  * { margin: 0; padding: 0; box-sizing: border-box; }
  html, body { width: 1200px; height: 945px; overflow: hidden; background: var(--page-bg); }
  .spread {
    position: relative; width: 1200px; height: 945px;
    display: flex; justify-content: center; align-items: center; gap: 80px;
  }
  .cover {
    position: relative; width: 400px; height: 555px; overflow: hidden;
    box-shadow: 0 6px 18px rgba(0,0,0,0.18);
  }
  .cover-art { position: absolute; inset: 0; }
  .cover-art--back {
    background: linear-gradient(180deg,
      var(--sky-grey) 0%, var(--sky-white) 22%, #dfe7ef 48%,
      var(--deep-blue) 58%, var(--sky-blue) 72%, #b9d58a 80%,
      var(--sun-yellow) 88%, var(--field-gold) 95%, var(--grass-dark) 100%);
  }
  .cover-art--front {
    background:
      radial-gradient(ellipse 60% 40% at 45% 30%, rgba(255,255,255,0.85), rgba(255,255,255,0) 70%),
      linear-gradient(180deg,
        var(--sky-blue) 0%, #bcdcf1 20%, var(--sky-white) 42%,
        #dbe6f0 55%, var(--deep-blue) 64%, var(--sky-blue) 72%,
        #b9d58a 80%, var(--sun-yellow) 88%, var(--field-gold) 95%, var(--grass-dark) 100%);
  }
  .cross-light {
    position: absolute; left: 50px; top: 60px; width: 175px; height: 305px;
    border-radius: 40px;
    background: radial-gradient(ellipse 55% 50% at 60% 45%, rgba(58,134,196,0.55), rgba(58,134,196,0.15) 70%, rgba(58,134,196,0) 100%);
  }
  .praying-figure {
    position: absolute; left: 266px; top: 426px; width: 46px; height: 118px;
    border-radius: 20px 20px 6px 6px;
    background: linear-gradient(180deg, var(--figure-teal) 0%, var(--figure-teal) 60%, var(--figure-dark) 100%);
    opacity: 0.85;
  }
  .blurb {
    position: absolute; left: 26px; right: 28px;
    font-family: "Lato", sans-serif; font-size: 10.9px; line-height: 13.9px; color: var(--ink);
  }
  .blurb p + p { margin-top: 13px; }
  .blurb--upper { top: 98px; }
  .blurb--lower { top: 336px; }
  .title {
    position: absolute; top: 92px; left: 0; right: 0; text-align: center;
    font-family: "Archivo Black", sans-serif; color: var(--title-blue);
    text-transform: uppercase; line-height: 1;
  }
  .title span { display: block; }
  .title__lg { font-size: 66px; letter-spacing: -1px; }
  .title__md { font-size: 82px; letter-spacing: -1px; }
  .title__sm { font-size: 46px; margin: 6px 0; }
  .subtitle {
    position: absolute; top: 375px; left: 30px; right: 30px; text-align: center;
    font-family: "Lato", sans-serif; font-size: 18px; line-height: 27px;
    color: var(--ink); text-transform: uppercase;
  }
  .author {
    position: absolute; top: 509px; left: 105px;
    font-family: "Montserrat", sans-serif; font-weight: 700; font-size: 15px;
    letter-spacing: 2.6px; color: var(--ink); text-transform: uppercase;
  }
</style>
</head>
<body>
  <main class="spread">
    <section class="cover cover--back">
      <div class="cover-art cover-art--back" role="img" aria-label="Photograph of a cloudy sky over a golden sunlit grass field"></div>
      <div class="blurb blurb--upper">
        <p>I want a book cover design, The book is a prayer book. Pleas no design with only words. I want something creative and original. Something that attracts attention just by looking at the cover. Something powerful. This book is for people that are experiencing issues and need prayer. This book is also for those that want to pray and pray effectively. Not only will there be prayers. But they will learn the dynamics of prayer and how to pray effectively and from the right position. This book is filled with power yet effective prayers that will.have the ability to break bondages off people lives.</p>
        <p>Below is some book covers that I found. I posted them to give an idea of what im looking for. Something that catches the attention of a reader.</p>
      </div>
      <div class="blurb blurb--lower">
        <p>I want a book cover design, The book is a prayer book. Pleas no design with only words. I want something creative and original. Something that attracts attention just by looking at the cover. Something powerful. This book is for people that are experiencing issues and need prayer. This book is also for those that want to pray and pray effectively. Not only will there be prayers. But they will learn the dynamics of prayer and how to pray effectively and from the right position. This book is filled with power yet effective prayers that will.have the ability to break bondages off people lives.</p>
        <p>Below is some book covers that I found. I posted them to give an idea of what im looking for. Something that catches the attention of a reader.</p>
      </div>
    </section>

    <section class="cover cover--front">
      <div class="cover-art cover-art--front" role="img" aria-label="Photograph of a bright cloudy sky above a golden field"></div>
      <div class="cross-light" role="img" aria-label="Glowing blue cross of light shining through the clouds"></div>
      <div class="praying-figure" role="img" aria-label="Woman standing in the field, seen from the side, raising her hands in prayer"></div>
      <h1 class="title">
        <span class="title__lg">Whispers</span>
        <span class="title__sm">at</span>
        <span class="title__md">Dawn</span>
      </h1>
      <p class="subtitle">Quiet Devotions for Every Weary Heart Seeking Rest</p>
      <p class="author">Author Name</p>
    </section>
  </main>
</body>
</html>
```